Looking for a cool & simple business-card-design for digital agency

Hi!

We are a web agency that offers Reputation Management, Vextra & Seo Services and software development. We like cool things, we like innovative styles.

We have uploaded our logo.

Project Deadline Extended Reason: Client does not want any designs with the colorful logo. Please send us submissions ONLY with the blac and white logo. What the client would like to see:1) Back of the card: is a silver logo on a black background2) front of the card with all the data, please use white background and black logo thank you Added Friday, May 8, 2015

```html
<!DOCTYPE html>
<html lang="en">
<head>
<meta charset="utf-8">
<title>Lumora AG – Stationery</title>
<link href="https://fonts.googleapis.com/css2?family=Questrial&family=Great+Vibes&display=swap" rel="stylesheet">
<style>
  :root {
    --backdrop: #cfcfcf;
    --paper: #fbfbfb;
    --ink: #1c1c1c;
    --ink-soft: #555555;
    --black-stock: #202020;
    --silver: #d9d9d9;
  }
  html, body { margin: 0; padding: 0; }
  body {
    width: 1200px; height: 1118px; overflow: hidden;
    background: var(--backdrop);
    font-family: "Questrial", sans-serif;
    color: var(--ink);
    position: relative;
  }
  .piece { position: absolute; box-sizing: border-box; overflow: hidden; }
  .paper { background: var(--paper); }
  .black { background: var(--black-stock); }

  .brand { display: flex; align-items: center; gap: 5px; font-weight: 400; color: var(--ink); white-space: nowrap; }
  .brand .mark { background: currentColor; display: inline-block; }
  .brand.light { color: var(--silver); }

  .letterhead { left: 188px; top: 62px; width: 425px; height: 539px; padding: 36px 36px 0 36px; font-size: 5.8px; line-height: 1.45; color: var(--ink-soft); }
  .letterhead .brand { font-size: 15px; }
  .letterhead .brand .mark { width: 12px; height: 12px; }
  .letterhead .date { margin-top: 48px; }
  .letterhead .recipient { margin-top: 6px; }
  .letterhead .salutation { margin-top: 34px; color: var(--ink); font-size: 6px; }
  .letterhead .body p { margin: 8px 0 0; text-align: justify; }
  .letterhead .closing { margin-top: 10px; display: flex; align-items: flex-start; gap: 10px; }
  .letterhead .closing strong { color: var(--ink); }
  .signature-area { width: 70px; height: 26px; background: linear-gradient(90deg, rgba(74,92,168,0.18), rgba(74,92,168,0.05)); }
  .letterhead .footer { position: absolute; left: 36px; bottom: 12px; font-size: 5px; }

  .folder { left: 617px; top: 47px; width: 416px; height: 554px; border-radius: 5px; }
  .folder .spine { position: absolute; left: 24px; top: 0; bottom: 0; width: 1px; background: #333; }
  .folder .brand { position: absolute; left: 116px; top: 76px; font-size: 22px; }
  .folder .brand .mark { width: 18px; height: 18px; }

  .envelope-front { left: 170px; top: 647px; width: 428px; height: 199px; padding: 20px 18px; font-size: 5.6px; color: var(--ink-soft); }
  .envelope-front .brand { font-size: 14px; margin-bottom: 6px; }
  .envelope-front .brand .mark { width: 11px; height: 11px; }

  .envelope-back { left: 616px; top: 647px; width: 416px; height: 199px; }
  .envelope-back svg { position: absolute; left: 0; top: 0; }

  .card { width: 163px; height: 92px; padding: 12px 12px 8px; font-size: 4.4px; color: var(--ink-soft); line-height: 1.35; }
  .card .brand { font-size: 10px; justify-content: flex-end; }
  .card .brand .mark { width: 8px; height: 8px; }
  .card-front { left: 196px; top: 893px; }
  .card-front .name { margin-top: 22px; color: var(--ink); font-size: 5px; letter-spacing: .2px; }
  .card-front .role { margin-bottom: 4px; }
  .card-back { left: 406px; top: 893px; }
  .card-back .brand { justify-content: flex-start; margin-left: 36px; }

  .slip { left: 616px; top: 893px; width: 416px; height: 178px; padding: 18px 26px; font-size: 5.2px; color: var(--ink-soft); }
  .slip .brand { font-size: 14px; }
  .slip .brand .mark { width: 11px; height: 11px; }
  .slip .compliments { font-family: "Great Vibes", cursive; font-size: 15px; color: var(--ink); margin-top: 92px; line-height: 1.2; }
</style>
</head>
<body>

<section class="piece paper letterhead" aria-label="Letterhead">
  <div class="brand"><span class="mark"></span>Lumora AG</div>
  <div class="date">30.02.2015</div>
  <div class="recipient">Recipient's name<br>Lindenweg 4<br>10115 Berlin<br>Germany</div>
  <div class="salutation">Dear sir,</div>
  <div class="body">
    <p>Good communication sits at the heart of every lasting partnership. We believe clear words build trust, and trust builds results that last for years. Whether by phone, video or in person, we keep our clients close and informed at every step of the way.</p>
    <p>In a world of fast messages and short attention, a printed letter still carries weight. It shows care, it stays on the desk, and it is read more than once. That is why we still choose paper for the moments that matter most to our partners.</p>
    <p>Every letter speaks for the company that sends it. We take care that tone, layout and detail reflect who we are and what we stand for in every message.</p>
    <p>Thank you for your time. We look forward to hearing from you and to shaping your next digital strategy together.</p>
  </div>
  <div class="closing">
    <div>Yours Sincerely,<br><strong>Lena Varga</strong></div>
    <div class="signature-area" role="img" aria-label="Handwritten signature"></div>
  </div>
  <div class="footer">18 Harbor Lane, Fairview, CA 90412<br><strong>Tel:</strong> +61 800-555-0142 · <strong>E-mail:</strong> info@lumora-ag.com · www.lumora-ag.com</div>
</section>

<section class="piece black folder" aria-label="Presentation folder">
  <div class="spine"></div>
  <div class="brand light"><span class="mark"></span>Lumora AG</div>
</section>

<section class="piece paper envelope-front" aria-label="Envelope front">
  <div class="brand"><span class="mark"></span>Lumora AG</div>
  <div>18 Harbor Lane<br>Fairview, CA 90412</div>
</section>

<section class="piece paper envelope-back" aria-label="Envelope back">
  <svg width="416" height="199" viewBox="0 0 416 199">
    <path d="M0 0 H416 V18 L386 58 H30 L0 18 Z" fill="var(--black-stock)"/>
    <rect x="202" y="22" width="12" height="12" fill="var(--silver)"/>
  </svg>
</section>

<section class="piece paper card card-front" aria-label="Business card front">
  <div class="brand"><span class="mark"></span>Lumora AG</div>
  <div class="name">JONAS KELLER</div>
  <div class="role">Managing Director</div>
  <div>18 Harbor Lane, Fairview, CA 90412<br>Tel: +61 800-555-0142<br>E-mail: info@lumora-ag.com</div>
</section>

<section class="piece black card card-back" aria-label="Business card back">
  <div class="brand light"><span class="mark"></span>Lumora AG</div>
</section>

<section class="piece paper slip" aria-label="Compliment slip">
  <div class="brand"><span class="mark"></span>Lumora AG</div>
  <div class="compliments">With Compliments</div>
  <div>18 Harbor Lane, Fairview, CA 90412<br><strong>Tel:</strong> +61 800-555-0142 · <strong>E-mail:</strong> info@lumora-ag.com · www.lumora-ag.com</div>
</section>

</body>
</html>
```